Massage-Creme label for a young pharmacy

We are a young pharmacy which is part of a big union. We developed for a customer a very good massage creme with aloe vera, coconut oil, and many more advantages and as well a massage jelly. All we need is a good and affordable label which is beatiful and helps us to promote our product. As we want to develop further products, it would be very cool to have a corporate label for all upcoming products.

Target Market(s)

professional masseurs and physiotherapists

Industry/Entity Type

Health And Wellness

Font styles to use
Sans Serif
Decorative

Colors

Designer to choose colors to be used in the design.

Requirements
Must have
• Professionally looking design (but I'm sure you are doing so... :-)
Nice to have
• Label can have any shape. What you see is just a bad label with corresponding sizes, so you can imagine how it would look like in the final state.
Should not have
• If possible, the label should not be completely black (although it might look cool) as we are printing it on our own Vostek qr318-ux and black is difficult to print (and very costy).

```html
<!DOCTYPE html>
<html lang="de">
<head>
<meta charset="utf-8">
<title>Massage Creme – Etikett</title>
<link rel="stylesheet" href="https://fonts.googleapis.com/css2?family=Share+Tech+Mono&family=Comfortaa:wght@700&family=Open+Sans:wght@400;600&display=swap">
<style>
  :root {
    --canvas-bg: #ececec;
    --label-bg: #ffffff;
    --label-glow: #f4f4f4;
    --orange: #f2883a;
    --green: #8cc63f;
    --pill: #a9c6d6;
    --pill-text: #ffffff;
    --tagline: #6f6f6f;
    --silver-dark: #3a3a3a;
    --silver-mid: #9a9a9a;
    --silver-light: #f5f5f5;
    --photo-green: #9fcf6a;
    --photo-brown: #7a4a2a;
  }
  html, body {
    margin: 0;
    padding: 0;
    overflow: hidden;
  }
  body {
    width: 1011px;
    height: 1200px;
    background: var(--canvas-bg);
    position: relative;
    font-family: "Open Sans", sans-serif;
  }
  .label {
    position: absolute;
    left: 39px;
    top: 110px;
    width: 933px;
    height: 980px;
    background: radial-gradient(ellipse at 50% 45%, var(--label-bg) 40%, var(--label-glow) 100%);
    border-radius: 0 0 40px 40px;
    overflow: hidden;
  }
  .silver-band {
    position: absolute;
    left: 0;
    width: 100%;
    height: 60px;
    background: linear-gradient(90deg,
      var(--silver-dark) 0%, var(--silver-mid) 6%, var(--silver-light) 25%,
      var(--silver-mid) 38%, var(--silver-light) 41%, var(--silver-dark) 48%,
      var(--silver-mid) 53%, var(--silver-light) 57%, var(--silver-light) 75%,
      var(--silver-mid) 92%, var(--silver-dark) 100%);
  }
  .silver-band--top { top: 0; height: 50px; }
  .silver-band--bottom { top: 565px; }
  .tagline {
    position: absolute;
    top: 150px;
    left: 0;
    width: 100%;
    text-align: center;
    font-family: "Share Tech Mono", monospace;
    font-size: 30px;
    letter-spacing: 7px;
    font-variant: small-caps;
    color: var(--tagline);
    margin: 0;
  }
  .veg-mark {
    position: absolute;
    top: 148px;
    right: 36px;
    width: 32px;
    height: 32px;
  }
  .product-name {
    position: absolute;
    top: 200px;
    left: 0;
    width: 100%;
    text-align: center;
    font-family: "Comfortaa", sans-serif;
    font-weight: 700;
    font-size: 150px;
    line-height: 1;
    color: var(--orange);
    margin: 0;
    letter-spacing: -2px;
  }
  .product-type {
    position: absolute;
    top: 405px;
    left: 184px;
    width: 530px;
    height: 70px;
    border-radius: 35px;
    background: var(--pill);
    color: var(--pill-text);
    font-family: "Open Sans", sans-serif;
    font-weight: 600;
    font-size: 50px;
    line-height: 70px;
    text-align: center;
    letter-spacing: 38px;
    text-indent: 38px;
  }
  .ingredients {
    position: absolute;
    top: 505px;
    left: 0;
    width: 100%;
    text-align: center;
    font-size: 34px;
    color: var(--tagline);
    margin: 0;
  }
  .ingredients__coconut { color: var(--orange); }
  .ingredients__aloe { color: var(--green); }
  .ingredient-photo {
    position: absolute;
    top: 635px;
    left: 195px;
    width: 505px;
    height: 265px;
    background: linear-gradient(90deg, var(--photo-green) 0%, #c8e6a8 45%, #b08a66 70%, var(--photo-brown) 100%);
  }
</style>
</head>
<body>
  <section class="label">
    <div class="silver-band silver-band--top"></div>

    <p class="tagline">Energetisch Leitend !</p>
    <svg class="veg-mark" viewBox="0 0 32 32" aria-hidden="true">
      <rect x="2" y="2" width="28" height="28" fill="none" stroke="#8cc63f" stroke-width="4"/>
      <circle cx="16" cy="16" r="8" fill="#8cc63f"/>
    </svg>

    <h1 class="product-name">Massage</h1>
    <div class="product-type">CREME</div>
    <p class="ingredients">
      <span class="ingredients__coconut">COCONUT</span> - <span class="ingredients__aloe">ALOEVERA</span>
    </p>

    <div class="silver-band silver-band--bottom"></div>

    <div class="ingredient-photo" role="img" aria-label="Photo of sliced aloe vera leaves with gel on a wooden spoon, and halved coconuts with splashing coconut milk and palm leaves"></div>
  </section>
</body>
</html>
```